Q7 Landing Page

We are looking for a creative landing page & a autosignature for our email.
The launchpage will be featuring a signupkite provided "widget"
All instructions are in the uploaded ZIP File
**Please note that we require the landing page back complete ready to be uploaded without having to do any modifications**
Reason: Awaiting some further submissions...

```html
<!DOCTYPE html>
<html lang="en">
<head>
<meta charset="utf-8">
<title>Q7 Studio — Landing Page</title>
<link rel="stylesheet" href="https://fonts.googleapis.com/css2?family=Ubuntu:wght@300;400;500&family=Open+Sans:wght@400;600&display=swap">
<style>
  :root {
    --accent: #7fc241;
    --accent-dark: #5c9a25;
    --ink: #ffffff;
    --ink-soft: #d6d6d6;
    --ink-muted: #a9a9a9;
    --bg-top: #000000;
    --bg-mid: #1c1c1c;
    --bg-bottom: #3b3b3b;
    --rule: #4a4a4a;
    --field: #ffffff;
    --field-text: #a6a6a6;
  }
  * { margin: 0; padding: 0; box-sizing: border-box; }
  html, body { width: 1200px; height: 900px; overflow: hidden; }
  body {
    position: relative;
    background: linear-gradient(to bottom, var(--bg-top) 0%, var(--bg-top) 30%, var(--bg-mid) 50%, var(--bg-bottom) 100%);
    font-family: "Ubuntu", sans-serif;
    color: var(--ink);
  }
  .top-bar { position: absolute; left: 0; top: 0; width: 1200px; height: 5px; background: var(--accent); }

  .brand { position: absolute; left: 52px; top: 72px; display: flex; align-items: center; gap: 20px; }
  .brand-square { width: 58px; height: 58px; background: var(--accent); }
  .brand-name { font-family: "Ubuntu", sans-serif; font-weight: 400; font-size: 44px; line-height: 1; color: var(--ink); }

  .device-visual {
    position: absolute; left: 73px; top: 220px; width: 234px; height: 462px;
    border-radius: 36px;
    background: linear-gradient(to bottom, #f4f4f4, #dcdcdc);
    box-shadow: 0 10px 18px rgba(0,0,0,0.45);
  }

  .headline { position: absolute; left: 377px; top: 248px; font-weight: 300; font-size: 35px; line-height: 42px; color: var(--ink); }
  .apps-label { position: absolute; left: 380px; top: 364px; font-size: 19px; font-weight: 400; color: var(--accent); }
  .apps-list { position: absolute; left: 398px; top: 398px; width: 244px; list-style: none; }
  .apps-list li {
    position: relative; height: 35px; line-height: 34px; padding-left: 30px;
    font-size: 17px; color: var(--ink); border-bottom: 1px solid #2a2a2a;
  }
  .apps-list li:last-child { border-bottom: none; }
  .apps-list li svg { position: absolute; left: 6px; top: 12px; }
  .cta-line { position: absolute; left: 386px; top: 533px; font-weight: 300; font-size: 25px; color: var(--ink); }

  .signup { position: absolute; left: 873px; top: 268px; width: 288px; }
  .signup-intro { font-family: "Open Sans", sans-serif; font-size: 12px; line-height: 21px; color: var(--ink); }
  .signup-form { display: flex; gap: 7px; margin-top: 9px; }
  .signup-field {
    width: 236px; height: 35px; background: var(--field); border: 1px solid #cfcfcf;
    font-family: "Open Sans", sans-serif; font-size: 14px; color: var(--field-text);
    padding: 0 11px; line-height: 34px;
  }
  .signup-go {
    width: 46px; height: 40px; margin-top: -2px; border-radius: 3px;
    background: linear-gradient(to bottom, #9ad45a, var(--accent-dark));
    border: 1px solid #4d8a1c;
    font-family: "Open Sans", sans-serif; font-weight: 600; font-size: 13px; color: var(--ink);
    text-align: center; line-height: 38px;
  }
  .signup-credit { margin-top: 15px; text-align: right; font-family: "Open Sans", sans-serif; font-size: 12px; color: var(--ink); }
  .signup-credit strong { font-weight: 600; font-size: 15px; }

  .social-band {
    position: absolute; left: 0; top: 760px; width: 1200px; height: 63px;
    border-top: 1px solid var(--rule); border-bottom: 1px solid var(--rule);
  }
  .social-label { position: absolute; left: 64px; top: 23px; font-family: "Open Sans", sans-serif; font-size: 16px; color: var(--ink-soft); }
  .social-icons { position: absolute; left: 200px; top: 11px; display: flex; gap: 14px; list-style: none; }
  .social-icons li {
    width: 40px; height: 40px; border-radius: 50%;
    background: radial-gradient(circle at 40% 35%, #ffffff, #d2d2d2);
    box-shadow: 0 2px 3px rgba(0,0,0,0.5);
  }

  .footer-note {
    position: absolute; left: 0; top: 855px; width: 1200px; text-align: center;
    font-family: "Open Sans", sans-serif; font-size: 12px; color: var(--ink-muted);
  }
  .footer-note span { margin: 0 6px; }
</style>
</head>
<body>
  <div class="top-bar"></div>

  <header class="brand">
    <div class="brand-square"></div>
    <div class="brand-name">Q7 Studio</div>
  </header>

  <div class="device-visual" role="img" aria-label="White smartphone showing the Q7 Studio name on its screen"></div>

  <h1 class="headline">Transferring the Web into<br>your Pocket</h1>
  <p class="apps-label">Instant Apps for:</p>
  <ul class="apps-list">
    <li><svg width="8" height="12" viewBox="0 0 8 12"><path d="M1 1l5 5-5 5" fill="none" stroke="#cccccc" stroke-width="1.4"/></svg>Industry</li>
    <li><svg width="8" height="12" viewBox="0 0 8 12"><path d="M1 1l5 5-5 5" fill="none" stroke="#cccccc" stroke-width="1.4"/></svg>Product Launches</li>
    <li><svg width="8" height="12" viewBox="0 0 8 12"><path d="M1 1l5 5-5 5" fill="none" stroke="#cccccc" stroke-width="1.4"/></svg>Viral Marketing Campaigns.</li>
  </ul>
  <p class="cta-line">For Mobile Solutions, come talk to us !</p>

  <section class="signup">
    <p class="signup-intro">Freedom.Delivered. Want to get mobile?<br>Let's have a talk</p>
    <div class="signup-form">
      <div class="signup-field">email@address.com</div>
      <div class="signup-go">GO</div>
    </div>
    <p class="signup-credit">powered by <strong>signupkite</strong></p>
  </section>

  <section class="social-band">
    <span class="social-label">Stay Connected</span>
    <ul class="social-icons">
      <li aria-label="Social network link"></li>
      <li aria-label="Social network link"></li>
      <li aria-label="Social network link"></li>
      <li aria-label="Social network link"></li>
    </ul>
  </section>

  <footer class="footer-note">© 2012 Company Name<span>|</span>Term &amp; Condition<span>|</span>All right reserved</footer>
</body>
</html>
```